Koorabin Vineyard

i need a wine label design. The name Koorabin can be hard to pronounce and hard to say, so looking for a clever way to have it written maybe koo-rabin. the attached picture is drawn by a local artist is a water colour of lily of the valley.
on the label we also need
Koorabin
Riesling
Clare Valley
2016

the wine style is elegant and boutique, if the picture attached could be used in its entirety or in a small way, that would be great.

Target Market(s)

Females 18 - 50

Industry/Entity Type

Vineyard

Logo Text

Koorabin

Logo styles of interest
Pictorial/Combination Logo
Abstract Logo
Character Logo
Wordmark Logo
Font styles to use
Serif
Decorative
Script

Requirements
Must have
• must be eye catching and vibrant
Nice to have
• elegance based around the picture attached, picture does not have to be the feature, or used at all, the picture was drawn by a local artist but does not have to be used. Koorabin is aboriginal for two hills and a water source, i.e dam/creek/stream
Should not have
• hard to read wording and text

```html
<!DOCTYPE html>
<html lang="en">
<head>
<meta charset="utf-8">
<title>Koorabin Riesling Label</title>
<link href="https://fonts.googleapis.com/css2?family=Cinzel:wght@400;700&display=swap" rel="stylesheet">
<style>
  :root {
    --paper: #ffffff;
    --ink: #111111;
    --art-tone: #e4e4e4;
  }
  html, body {
    margin: 0;
    padding: 0;
    width: 1200px;
    height: 720px;
    overflow: hidden;
    background: var(--paper);
  }
  .canvas {
    position: relative;
    width: 1200px;
    height: 720px;
    background: var(--paper);
    color: var(--ink);
    font-family: "Cinzel", Georgia, serif;
  }
  .label-frame {
    position: absolute;
    left: 325px;
    top: 97px;
    width: 522px;
    height: 507px;
    border: 4px solid var(--ink);
  }
  .flower-art {
    position: absolute;
    left: 388px;
    top: 163px;
    width: 410px;
    height: 134px;
  }
  .wordmark {
    position: absolute;
    left: 325px;
    width: 530px;
    top: 340px;
    margin: 0;
    text-align: center;
    font-weight: 400;
    font-size: 66px;
    line-height: 1;
    letter-spacing: 2px;
    color: var(--ink);
  }
  .varietal {
    position: absolute;
    left: 325px;
    width: 530px;
    top: 456px;
    margin: 0;
    text-align: center;
    font-weight: 700;
    font-size: 30px;
    line-height: 1;
    letter-spacing: 2px;
  }
  .region {
    position: absolute;
    left: 325px;
    width: 530px;
    top: 487px;
    margin: 0;
    text-align: center;
    font-size: 14px;
    line-height: 1;
    letter-spacing: 1.5px;
  }
  .vintage {
    position: absolute;
    left: 325px;
    width: 530px;
    top: 543px;
    margin: 0;
    text-align: center;
    font-size: 15px;
    line-height: 1;
    letter-spacing: 1px;
  }
</style>
</head>
<body>
  <main class="canvas">
    <div class="label-frame"></div>

    <svg class="flower-art" viewBox="0 0 410 134" role="img" aria-label="Hand-drawn lily of the valley bloom resting on a sweeping line of two hills">
      <rect x="0" y="0" width="410" height="134" rx="10" fill="var(--art-tone)"/>
    </svg>

    <h1 class="wordmark">koo-rabin</h1>
    <p class="varietal">Riesling</p>
    <p class="region">Clare Valley</p>
    <p class="vintage">2016</p>
  </main>
</body>
</html>
```